Website for a financial survey consultancy

WHO WE ARE
We're a niche HR consultancy specialising in salary comparison surveys for the financial asset management industry. We position ourselves as a small, highly responsive organisation with a strong personal relationship with each of our 50+ blue-chip clients.

WHAT WE DO
Our business is 80% surveys (= products), 20% consultancy (= services). The surveys are a set of online products which clients interact with to find the information they are interested in.

WHAT WE WANT
We are completely revising our existing marketing website and need a new up-to-date look and feel for the site. We want you to design 2 web pages
- Home page
- Internal content page

More details below in Must Have Priorities.

REFERENCE SITES
- www.tallowmere.com - nice background image
- www.quimbelt.com - ignoring the animations
- www.palvastro.com
- www.dulmiko.com - clean, fresh, styly but prob not corporate enough
- www.orvettagrove.com - spacious, beautiful, slightly dated tho
- www.plinzer.co.uk - ignore the colours. Like the simplicity, larger font size (although want to stick with sans-serif fonts for main content)

DELIVERABLES
The final designs should be delivered as one or more PSD files with clearly named layers. All design elements and treatments should be separated out, for example use adjustment layers rather than applied (and subsequently irreversible) adjustments, strokes, shading, etc.

WHAT NEXT
I'll be monitoring the contest every day and can respond to questions fast. You can IM me on Skype or MSN.

Reason: Hi folks,

I am extending the deadline to this project as I am travelling this week and therefore will not be able to make a final decision until next Monday. I will try and provide further feedback over the course of this week but I am only going to be online occasionally so be prepared to wait a few days for a reply from me.

Thanks for all the designs so far.

Owen

Target Market(s)

In order of importance, most important first

1. Potential customers - UK & US financial industry HR professionals, short on time. Heard about us already, want to find out more about what we do, confirm relevance for their needs. Core goal - establish credibility: are we properly resourced, will we be around for years to come, are we *real*.

2. Existing customers - UK & US financial industry professionals, short on time, under pressure, want results quickly, minimum faff, expect high quality, slickly presented information. Primary action: login and use surveys.

3. Industry professionals/researchers - probably arriving through blog content, looking to browse and hoover information. Valuable for their ability to spread awareness of who we are amongst their peers.

Industry/Entity Type

Financial

Requirements
Must have
• GENERAL
Style cues - Corporate, professional, financial, stylish, slick, clean, spacious, light
Size - standard 960px grid

NAVIGATION
- [ Home | About us | Surveys | Consulting | Blog ]
- Sub-nav (roll-over dropdown) on About Us, Surveys & Consulting

ALL PAGES
- Site navigation
- Client login (on screen permanently or link to ajaxy in-page pop-up)
- Footer section
- Existing logo (attached)* - this is obviously an important reference point in the design, esp colour

HOME PAGE
- Communicate (link thru to?) survey/consulting split
- Large photo(s)/backdrop (2-3 interchangeable options ideally). Please consider what rights agreement will be necessary for any photos you include in your design.
- Possibly bigger more prominent version of logo
- Strap line/sentence - "Focussed data is the key to success"
- 3 recent blog posts (should look good with and without blog post images)
- Free downloadable PDF research report + supporting blurb

INTERNAL PAGE
- Page title
- Content - typical page will be less than one screenfull
- Level 1 sub-heading
- Level 2 sub-heading
- Bulleted list
- Content supporting image (any image will do - interested in placement, borders (if any), spacing, caption, etc)
- 'Do something' button

* Note: there is some internal debate about this logo at the moment. Some (me) are keen for it to change, some (not me!) are not. If you have an web page design idea/concept that requires an evolution of the logo, go ahead and evolve it. We can explore this further in the design process as necessary, but don't sweat it.
Nice to have
• Values to communicate
- Knowledgeable
- Professional
- Secure
- Personal
- Experienced
- Financial industry specific
- Accurate
- Reliable
Should not have
• - Search box
- Social media links, other than RSS feed button (discrete)

```html
<!DOCTYPE html>
<html lang="en">
<head>
<meta charset="utf-8">
<title>Torvane Consulting – Home</title>
<link href="https://fonts.googleapis.com/css2?family=Arimo:wght@400;700&family=Questrial&family=Oswald:wght@300;400&display=swap" rel="stylesheet">
<style>
:root{
  --brand:#6b0c0c;
  --page:#f4f3f1;
  --text:#444;
  --muted:#666;
  --nav:#555;
  --footer:#d3d1cc;
  --bubble:#bab9b3;
  --frame:#cfcecb;
}
*{margin:0;padding:0;box-sizing:border-box}
html,body{width:1200px;height:1144px;overflow:hidden;background:var(--page)}
body{font-family:"Arimo",Arial,sans-serif;color:var(--text)}
.site{position:relative;width:1200px;height:1144px;overflow:hidden}
.abs{position:absolute}

/* brand */
.brand{left:119px;top:24px;display:flex;align-items:center;gap:10px}
.brand-square{width:18px;height:18px;background:var(--brand)}
.brand-name{font-size:30px;color:var(--brand)}

/* navigation */
.main-nav{left:577px;top:0;display:flex;height:65px;align-items:center;font-size:16px;color:var(--nav)}
.main-nav a{color:inherit;text-decoration:none;height:65px;line-height:78px;padding:0 17px}
.main-nav a.active{background:var(--brand);color:#fff}
.main-nav a:last-child{padding-right:0}

/* hero */
.hero{left:269px;top:65px;width:812px;height:295px;border:5px solid var(--frame);box-shadow:0 8px 8px -4px rgba(0,0,0,.2)}
.hero-photo{position:absolute;inset:0;background:
  linear-gradient(180deg,rgba(0,0,0,0) 60%,rgba(60,50,40,.5) 100%),
  linear-gradient(180deg,#6b6a66 0%,#d8c28a 30%,#f2b33c 52%,#c58f42 62%,#8d7d6a 80%,#6b645c 100%)}
.hero-tagline{position:absolute;right:0;bottom:0;width:425px;height:132px;background:rgba(190,160,120,.45);
  font-family:"Questrial",sans-serif;font-size:35px;color:#f6dfb6;padding:44px 0 0 30px;white-space:nowrap}

/* profile */
.profile{left:119px;top:396px;width:660px}
.profile h1{font-weight:400;font-size:38px;color:var(--brand);margin-bottom:8px}
.profile p{font-size:14.5px;line-height:18px;margin-bottom:17px}
.download{left:824px;top:440px;width:257px;height:84px;border-radius:0 8px 8px 0;
  background:linear-gradient(180deg,#f7f7f6 0%,#e9e9e8 50%,#d9d9d8 51%,#dcdcdb 100%)}
.download-line{left:823px;top:405px;width:2px;height:155px;background:linear-gradient(180deg,transparent,#bbb 40%,#bbb 60%,transparent)}
.download-icon{left:852px;top:454px;width:58px;height:60px;background:var(--brand)}
.download-title{left:924px;top:452px;font-family:"Oswald",sans-serif;font-weight:300;font-size:29px;line-height:30px;color:#333}
.download-sub{left:924px;top:487px;font-family:"Oswald",sans-serif;font-weight:300;font-size:17px;color:#333}

.divider{left:119px;top:584px;width:959px;border-top:1px dotted #bbb}
.col-divider{left:597px;top:620px;height:190px;border-left:1px dotted #bbb}

/* feature columns */
.feature h2{font-weight:400;font-size:31px;color:var(--brand);position:absolute;top:0;left:0;white-space:nowrap}
.feature-photo{position:absolute;top:45px;left:0;width:218px;height:144px;border:1px solid #ccc}
.feature-text{position:absolute;top:43px;left:225px;width:229px;font-size:12.5px;line-height:15px;letter-spacing:.35px;text-align:justify;color:#444}
.feature-text p{margin-bottom:15px}
.read-more{position:absolute;top:180px;right:2px;font-size:12.5px;letter-spacing:.3px;color:var(--brand);text-decoration:underline}
.surveys{left:119px;top:616px;width:454px;height:200px}
.consultancy{left:620px;top:616px;width:454px;height:200px}
.surveys .feature-photo{background:linear-gradient(135deg,#f2f2f2,#cfcfcf 60%,#e9e9e9)}
.consultancy .feature-photo{background:linear-gradient(180deg,#8a8a8a,#c4c4c4 55%,#efefef)}

/* footer */
.footer{left:0;top:844px;width:1200px;height:300px;background:var(--footer)}
.footer h3{position:absolute;font-weight:400;font-size:29px;color:#444}
.blog-title{left:119px;top:26px}
.blog-bubble{left:119px;top:102px;width:483px;height:166px;background:var(--bubble);border:2px solid #adaca6;padding:20px 18px;font-size:12.5px;line-height:19px;letter-spacing:.25px;color:#555}
.blog-bubble p{margin-bottom:18px}
.bubble-tail{left:186px;top:74px}
.foot-rule{top:31px;height:240px;border-left:1px solid #b7b5b0}
.sitemap-title{left:696px;top:26px}
.sitemap{left:698px;top:71px;font-size:12.5px;line-height:18.8px;color:var(--muted);list-style:none;letter-spacing:.2px}
.sitemap .top{font-weight:700}
.sitemap .sub{padding-left:8px}
.contact-title{left:909px;top:26px}
.contact{left:910px;top:71px;font-size:12.5px;line-height:15.5px;color:#444}
.contact p{margin-bottom:19px}
.contact-rule{left:909px;top:191px;width:171px;border-top:1px solid #b0aea9}
.copy-mark{left:909px;top:212px}
.copyright{left:910px;top:256px;font-size:9.8px;color:#444;white-space:nowrap}
</style>
</head>
<body>
<div class="site">
  <div class="abs brand"><span class="brand-square"></span><span class="brand-name">Torvane</span></div>

  <nav class="abs main-nav">
    <a class="active" href="#">Home</a><a href="#">About us</a><a href="#">Surveys</a><a href="#">Consulting</a><a href="#">Blog</a><a href="#">Login</a>
  </nav>

  <div class="abs hero">
    <div class="hero-photo" role="img" aria-label="Photo of a lighthouse on a rocky shore at sunset"></div>
    <div class="hero-tagline">Guiding you to Success</div>
  </div>

  <section class="abs profile">
    <h1>Company Profile</h1>
    <p>Lorem Ipsum is simply dummy text of the printing and typesetting industry. Lorem Ipsum has been the industry's standard dummy text.</p>
    <p>When an unknown printer took a galley of type and scrambled it to make a type specimen book. It has survived not only five centuries, but also the leap into electronic typesetting, remaining essentially un-changed.</p>
  </section>

  <div class="abs download-line"></div>
  <div class="abs download"></div>
  <div class="abs download-icon"></div>
  <div class="abs download-title">Download</div>
  <div class="abs download-sub">research report</div>

  <div class="abs divider"></div>
  <div class="abs col-divider"></div>

  <section class="abs feature surveys">
    <h2>Surveys</h2>
    <div class="feature-photo" role="img" aria-label="Photo of a pen resting on a survey answer sheet"></div>
    <div class="feature-text">
      <p>Lorem Ipsum is simply dummy text of the printing and typesetting industry. Lorem Ipsum has been the industry's standard dummy text.</p>
      <p>When an unknown printer took a galley of type and scrambled it to make a type specimen book.</p>
    </div>
    <a class="read-more" href="#">read more</a>
  </section>

  <section class="abs feature consultancy">
    <h2>Consultancy</h2>
    <div class="feature-photo" role="img" aria-label="Photo of a signpost pointing to support, help, advice and guidance"></div>
    <div class="feature-text">
      <p>Lorem Ipsum is simply dummy text of the printing and typesetting industry. Lorem Ipsum has been the industry's standard dummy text.</p>
      <p>When an unknown printer took a galley of type and scrambled it to make a type specimen book.</p>
    </div>
    <a class="read-more" href="#">read more</a>
  </section>

  <footer class="abs footer">
    <h3 class="blog-title">Blog</h3>
    <svg class="abs bubble-tail" width="36" height="30" viewBox="0 0 36 30"><path d="M1 0 L34 30 L1 30 Z" fill="var(--bubble)"/><path d="M1 0 L34 28" stroke="#adaca6" stroke-width="2" fill="none"/></svg>
    <div class="abs blog-bubble">
      <p>• Lorem Ipsum is simply dummy text of the printing and typesetting industry. Lorem Ipsum has been the industry's standard dummy text.</p>
      <p>• When an unknown printer took a galley of type and scrambled it to make a type specimen book.</p>
      <p>• It has survived not only five but also the leap into electronic.</p>
    </div>

    <div class="abs foot-rule" style="left:646px"></div>
    <div class="abs foot-rule" style="left:851px"></div>

    <h3 class="sitemap-title">Sitemap</h3>
    <ul class="abs sitemap">
      <li class="top">Home</li>
      <li class="top">About Us</li>
      <li class="sub">Sub Page1</li>
      <li class="sub">Sub Page2</li>
      <li class="top">Surveys</li>
      <li class="sub">Sub Page1</li>
      <li class="sub">Sub Page2</li>
      <li class="top">Consulting</li>
      <li class="sub">Sub Page1</li>
      <li class="top">Blog</li>
      <li class="top">Contact</li>
    </ul>

    <h3 class="contact-title">Contact</h3>
    <address class="abs contact" style="font-style:normal">
      <p>Torvane Consulting Ltd<br>14 Mercer Row<br>London EC2N 4QT</p>
      <p>+44 (0)20 7946 0812<br>info@torvaneconsulting.com</p>
    </address>
    <div class="abs contact-rule"></div>
    <svg class="abs copy-mark" width="28" height="28" viewBox="0 0 28 28"><circle cx="14" cy="14" r="12" fill="none" stroke="#333" stroke-width="2.2"/><path d="M18.5 10.2 A6 6 0 1 0 18.5 17.8" fill="none" stroke="#333" stroke-width="2.2"/></svg>
    <div class="abs copyright">2011 Copyright torvaneconsulting.com</div>
  </footer>
</div>
</body>
</html>
```